Chicken Wing A0 and A4 Poster

Our restaurant name is Tavlo Grill

We have introduced chicken wings to our menu. They are deep fried and mixed with different sauce selections.

The sauce options are: Tavlo BBQ, Regular BBQ, Sweet Chili and Garlic, Hot Chili, Garlic

Available in a 6, 10 or 20 Pack.
Larger Catering Packs Available

We have uploaded some pictures from the internet with chicken wings.

We also have 4 other poster designs coming in the next 3 weeks.

Restaurant

```html
<!DOCTYPE html>
<html lang="en">
<head>
<meta charset="utf-8">
<title>Tavlo Grill – Chicken Wings Poster</title>
<link rel="stylesheet" href="https://fonts.googleapis.com/css2?family=Archivo+Black&family=Roboto:wght@900&display=swap">
<style>
  :root {
    --maroon: #a52845;
    --white: #ffffff;
    --cream: #fbf3ee;
    --peach: #f6b48c;
    --orange: #f2802f;
    --deep-orange: #d9561d;
    --wing-red: #a8340f;
    --wing-gold: #f0a04a;
    --wing-brown: #7a2a0c;
    --dip: #f4e6d8;
  }
  html, body {
    margin: 0;
    padding: 0;
    width: 899px;
    height: 1200px;
    overflow: hidden;
    background: #ffffff;
  }
  .poster {
    position: relative;
    width: 899px;
    height: 1200px;
    overflow: hidden;
    font-family: "Archivo Black", "Arial Black", sans-serif;
    color: var(--maroon);
    background:
      radial-gradient(ellipse 420px 380px at 160px 160px, var(--cream) 0%, rgba(251,243,238,0) 100%),
      radial-gradient(ellipse 520px 500px at 800px 700px, var(--deep-orange) 0%, rgba(217,86,29,0) 100%),
      linear-gradient(115deg, #f9e3d6 0%, var(--peach) 35%, var(--orange) 70%, var(--deep-orange) 100%);
  }
  .wings-photo {
    position: absolute;
    left: 0;
    top: 780px;
    width: 899px;
    height: 420px;
    background:
      radial-gradient(ellipse 60px 120px at 20px 150px, var(--dip) 0%, rgba(244,230,216,0) 100%),
      radial-gradient(ellipse 300px 90px at 420px 190px, var(--wing-gold) 0%, rgba(240,160,74,0) 100%),
      radial-gradient(ellipse 200px 120px at 700px 250px, var(--wing-brown) 0%, rgba(122,42,12,0) 100%),
      radial-gradient(ellipse 520px 260px at 450px 260px, var(--wing-red) 0%, rgba(168,52,15,0) 100%),
      linear-gradient(180deg, rgba(217,86,29,0) 0%, #c24e1c 22%, #9e3512 100%);
  }
  .brand {
    position: absolute;
    left: 64px;
    top: 178px;
    width: 760px;
    margin: 0;
    font-size: 128px;
    line-height: 1;
    letter-spacing: -3px;
    white-space: nowrap;
    color: var(--maroon);
  }
  .tagline {
    position: absolute;
    left: 96px;
    top: 344px;
    width: 680px;
    margin: 0;
    font-size: 31px;
    letter-spacing: 6px;
    text-align: center;
    white-space: nowrap;
    transform: rotate(-5deg);
  }
  .available {
    position: absolute;
    left: 0;
    top: 410px;
    width: 899px;
    margin: 0;
    font-family: "Roboto", "Arial", sans-serif;
    font-weight: 900;
    font-size: 23px;
    letter-spacing: 1px;
    text-align: center;
    transform: rotate(-2deg);
  }
  .pack {
    position: absolute;
    width: 168px;
    height: 168px;
  }
  .pack-6  { left: 140px; top: 472px; }
  .pack-10 { left: 363px; top: 442px; }
  .pack-20 { left: 585px; top: 404px; }
  .pack text { fill: var(--maroon); }
  .pack .pack-label { font-family: "Roboto", "Arial", sans-serif; font-weight: 900; font-size: 14px; letter-spacing: 1px; }
  .pack .pack-count { font-family: "Roboto", "Arial", sans-serif; font-weight: 900; font-size: 58px; }
  .pack .pack-mark { font-family: "Roboto", "Arial", sans-serif; font-weight: 900; font-size: 22px; }
  .catering {
    position: absolute;
    left: 130px;
    top: 640px;
    width: 680px;
    margin: 0;
    font-family: "Roboto", "Arial", sans-serif;
    font-weight: 900;
    font-size: 34px;
    line-height: 1;
    text-align: center;
    white-space: nowrap;
    transform: rotate(-4deg);
  }
  .sauce-band {
    position: absolute;
    left: 150px;
    top: 680px;
    width: 640px;
    height: 40px;
    background: var(--white);
    transform: rotate(-4deg);
    display: flex;
    align-items: center;
    justify-content: space-between;
    padding: 0 14px;
    box-sizing: border-box;
    font-family: "Roboto", "Arial", sans-serif;
    font-weight: 900;
    color: var(--maroon);
  }
  .sauce-band .stars { font-size: 18px; letter-spacing: 22px; }
  .sauce-band .band-title { font-size: 22px; letter-spacing: 0.5px; }
  .sauce-list {
    position: absolute;
    left: 130px;
    top: 730px;
    width: 680px;
    margin: 0;
    font-family: "Roboto", "Arial", sans-serif;
    font-weight: 900;
    font-size: 25px;
    line-height: 1.2;
    color: var(--white);
    text-align: center;
    transform: rotate(-4deg);
  }
</style>
</head>
<body>
<main class="poster">
  <div class="wings-photo" role="img" aria-label="Close-up photo of saucy deep-fried chicken wings with a dip on the side"></div>

  <h1 class="brand">Tavlo Grill</h1>

  <p class="tagline">AUTHENTIC LEBANESE FOOD</p>
  <p class="available">AVAILABLE IN A</p>

  <svg class="pack pack-6" viewBox="0 0 172 172" role="img" aria-label="Pack of 6">
    <defs><path id="arc6" d="M28,92 A58,58 0 0 1 144,92"/></defs>
    <circle cx="86" cy="86" r="86" fill="#fff"/>
    <text class="pack-label"><textPath href="#arc6" startOffset="8%">PACK OF ★ ★ ★ ★</textPath></text>
    <text class="pack-mark" x="44" y="130">×</text>
    <text class="pack-count" x="86" y="124" text-anchor="middle">6</text>
    <text class="pack-mark" x="112" y="118">×</text>
  </svg>

  <svg class="pack pack-10" viewBox="0 0 172 172" role="img" aria-label="Pack of 10">
    <defs><path id="arc10" d="M28,92 A58,58 0 0 1 144,92"/></defs>
    <circle cx="86" cy="86" r="86" fill="#fff"/>
    <text class="pack-label"><textPath href="#arc10" startOffset="8%">PACK OF ★ ★ ★ ★</textPath></text>
    <text class="pack-mark" x="30" y="130">×</text>
    <text class="pack-count" x="86" y="124" text-anchor="middle">10</text>
    <text class="pack-mark" x="126" y="118">×</text>
  </svg>

  <svg class="pack pack-20" viewBox="0 0 172 172" role="img" aria-label="Pack of 20">
    <defs><path id="arc20" d="M28,92 A58,58 0 0 1 144,92"/></defs>
    <circle cx="86" cy="86" r="86" fill="#fff"/>
    <text class="pack-label"><textPath href="#arc20" startOffset="8%">PACK OF ★ ★ ★ ★</textPath></text>
    <text class="pack-mark" x="30" y="130">×</text>
    <text class="pack-count" x="86" y="124" text-anchor="middle">20</text>
    <text class="pack-mark" x="126" y="118">×</text>
  </svg>

  <p class="catering">LARGER CATERING PACKS AVAILABLE</p>

  <div class="sauce-band">
    <span class="stars">★★★</span>
    <span class="band-title">THE SAUCE OPTIONS ARE</span>
    <span class="stars">★★★</span>
  </div>

  <p class="sauce-list">TAVLO BBQ, REGULAR BBQ, SWEET CHILI AND<br>GARLIC, HOT CHILI, GARLIC</p>
</main>
</body>
</html>
```